Simple web design project

We need a four page web design for a premier domestic cleaning company. We would like to see designs which use white and blue (the blue in the logo - which is attatched). Please could the tab for the pages be horizontal and at the top of the page. Our company logo is attached and should be included on each page. Ideally, we would like the foundations of each page to be the same, with the word content differing as required (word content attatched). Additionally we have attached a flyer which has been distributed to advertise our company. Please could all web designs illustrate the same professional message this flyer does.

Target Market(s)

females with higher than average income, aged 30-50. Have families and work 9-5.

Industry/Entity Type

It Company

Requirements
Must have
• logo on each page. Foundations of each page the same. phone number and email on the bottom of each page.
Should not have
• please no pictures of females cleaning.

```html
<!DOCTYPE html>
<html lang="en">
<head>
<meta charset="utf-8">
<title>Brightwell Cleaners – Premier Domestic Cleaners</title>
<link href="https://fonts.googleapis.com/css2?family=Open+Sans:wght@400;600;700&family=PT+Sans:wght@400;700&display=swap" rel="stylesheet">
<style>
:root{
  --blue:#1a9ad6;
  --blue-dark:#1378b4;
  --link:#1a86c4;
  --orange:#f7941d;
  --text:#4a4a4a;
  --muted:#777;
  --light:#f0f0f0;
  --btn:#3c3c3c;
  --footer:#303030;
  --footer-bottom:#1f1f1f;
  --footer-text:#d8d8d8;
}
*{box-sizing:border-box;margin:0;padding:0}
html,body{width:800px;height:1200px;overflow:hidden}
body{position:relative;background:#fff;font-family:"Open Sans",Arial,sans-serif;color:var(--text);font-size:8.5px;line-height:1.6}
.abs{position:absolute}
h2{font-family:"PT Sans",Arial,sans-serif;font-weight:400;color:var(--link);font-size:19px;line-height:1}
a{color:inherit;text-decoration:none}

/* header */
.site-header{left:0;top:0;width:800px;height:118px;background:linear-gradient(#fff,#ececec);border-bottom:1px solid #d6d6d6}
.header-swoosh{left:0;top:0}
.brand{left:86px;top:50px;color:#fff}
.brand-name{font-family:"PT Sans",Arial,sans-serif;font-size:20px;font-weight:700;display:flex;align-items:center;gap:6px;line-height:1}
.brand-mark{width:14px;height:14px;background:#fff;border-radius:50%}
.brand-tag{font-size:8px;font-weight:600;margin:6px 0 0 32px}
.call{left:570px;top:8px;color:var(--blue)}
.call-label{font-size:10px;color:#444;margin-left:26px}
.call-number{font-family:"PT Sans",Arial,sans-serif;font-size:20px;display:flex;align-items:center;gap:4px;line-height:1}
.main-nav{left:353px;top:69px;width:361px;height:31px;background:linear-gradient(#5a5a5a,#2e2e2e);border-radius:3px;display:flex;box-shadow:0 3px 4px rgba(0,0,0,.3)}
.main-nav a{flex:1;color:#fff;font-size:9.5px;display:flex;align-items:center;justify-content:center;border-right:1px solid #222;border-left:1px solid #666}
.main-nav a:first-child{border-left:0}.main-nav a:last-child{border-right:0}

/* hero */
.hero{left:86px;top:123px;width:628px;height:270px;border:1px solid #ddd;background:#fff;padding:3px}
.hero-inner{position:relative;width:100%;height:100%;background:linear-gradient(#f6f6f6,#dcdcdc);overflow:hidden}
.hero-photo{left:152px;top:0;width:468px;height:262px;background:linear-gradient(135deg,#c7c9d3 0%,#b4b8c6 50%,#a7acbd 100%);border-left:4px solid var(--blue);border-radius:80px 0 0 0}
.hero-title{left:18px;top:44px;font-family:"PT Sans",Arial,sans-serif;font-weight:700;font-size:31px;line-height:1;color:#3d3d3d}
.hero-badge{left:16px;top:128px;width:132px;height:62px;background:var(--orange);border-radius:50%}
.hero-badge-text{left:16px;top:128px;width:132px;height:62px;display:flex;align-items:center;justify-content:center;text-align:center;font-family:"PT Sans",Arial,sans-serif;font-weight:700;font-size:11px;line-height:1.15;color:#fff}
.hero-free{left:18px;top:203px;font-family:"PT Sans",Arial,sans-serif;font-weight:700;font-size:20px;color:#333;line-height:1}
.hero-free b{font-size:26px;border-bottom:3px solid var(--orange)}
.hero-sub{left:18px;top:234px;font-family:"PT Sans",Arial,sans-serif;font-weight:700;font-size:11px;color:#333}
.dots{right:16px;top:10px;display:flex;gap:4px}
.dots span{width:11px;height:11px;border-radius:50%;background:#888}
.dots span:first-child{background:#333}

/* content */
.welcome-photo{left:86px;top:448px;width:190px;height:68px;background:linear-gradient(#e8e4df,#b77b4a)}
.intro-strong{font-weight:600}
.para{width:190px}
.btn{display:inline-block;background:var(--btn);color:#fff;font-weight:700;font-size:9px;padding:3px 9px;border-radius:2px}
.list{list-style:none}
.list li{color:var(--link);font-weight:600;padding-left:14px;position:relative;margin-bottom:7px;line-height:1.3}
.list li::before{content:"";position:absolute;left:0;top:3px;width:5px;height:5px;border-radius:50%;background:var(--orange)}
.list li span{color:var(--text);font-weight:400}

.quote{left:514px;top:448px;width:200px;height:207px;background:var(--light);border:1px solid #e2e2e2;padding:8px 12px;box-shadow:0 4px 4px -2px rgba(0,0,0,.15)}
.quote label{display:block;font-size:8.5px;margin-bottom:2px}
.field{height:21px;background:#fff;border:1px solid #cfcfcf;border-radius:2px;margin-bottom:7px}
.field-row{display:flex;gap:13px}
.field-row>div{flex:1}
.select{height:21px;border:1px solid #cfcfcf;background:linear-gradient(#fff,#e9e9e9);font-size:7.5px;color:#888;padding:4px 8px;display:flex;justify-content:space-between;border-radius:2px}
.btn-orange{background:linear-gradient(#fdb14a,var(--orange));color:#fff;font-weight:600;font-size:9px;padding:3px 9px;border-radius:3px;display:inline-block}

.why-photo{left:86px;top:714px;width:94px;height:181px;background:linear-gradient(#c9ccd0,#7b8796)}
.price-row{display:flex;align-items:baseline;font-size:8px;width:297px}
.price-row .dash{flex:1;border-bottom:1px dashed #999;margin:0 2px}
.price-row b{font-size:10px;font-weight:600;color:#333}

/* footer */
.site-footer{left:0;top:913px;width:800px;height:244px;background:linear-gradient(var(--footer),#3a3a3a);color:var(--footer-text)}
.site-footer h3{font-family:"PT Sans",Arial,sans-serif;font-weight:400;font-size:13.5px;color:#fff}
.site-footer h4{font-size:9.5px;font-weight:600;color:#fff;line-height:1.2}
.map{left:86px;top:42px;width:174px;height:132px;background:linear-gradient(135deg,#f2e9c8,#e6dcae);border:1px solid #999}
.qfield{width:172px;height:21px;background:linear-gradient(#fff,#e2e2e2);border-radius:3px;color:#444;font-size:8.5px;padding:4px 8px}
.small{font-size:7.5px;line-height:1.6}
.orange{color:var(--orange)}
.footer-bottom{left:0;top:1157px;width:800px;height:43px;background:var(--footer-bottom);color:#bbb}
.social{display:flex;gap:7px}
.social span{width:21px;height:21px;border-radius:3px;display:block}
</style>
</head>
<body>

<header class="site-header abs">
  <svg class="header-swoosh abs" width="430" height="118" viewBox="0 0 430 118">
    <defs><linearGradient id="sw" x1="0" y1="0" x2="1" y2="1"><stop offset="0" stop-color="#2aa8e2"/><stop offset="1" stop-color="#1283c4"/></linearGradient></defs>
    <path d="M0 0H425C340 10 285 50 265 118H0Z" fill="url(#sw)"/>
    <path d="M425 0C340 10 285 50 265 118" stroke="#fff" stroke-width="6" fill="none" opacity=".8"/>
  </svg>
  <div class="brand abs">
    <div class="brand-name"><span class="brand-mark"></span>Brightwell Cleaners</div>
    <div class="brand-tag">Premier Domestic Cleaners</div>
  </div>
  <div class="call abs">
    <div class="call-label">Call Us</div>
    <div class="call-number">
      <svg width="20" height="18" viewBox="0 0 20 18"><path d="M3 2c2-2 4 0 5 2s0 2-1 3c1 2 3 4 5 5 1-1 1-2 3-1s4 3 2 5c-2 2-6 1-10-3S1 4 3 2z" fill="#555"/></svg>
      07700900461
    </div>
  </div>
  <nav class="main-nav abs">
    <a href="#">HOME</a><a href="#">SERVICES</a><a href="#">PRICES</a><a href="#">CONTACT US</a>
  </nav>
</header>

<section class="hero abs">
  <div class="hero-inner">
    <div class="hero-photo abs" role="img" aria-label="Gloved hands scrubbing a tiled floor with a sponge beside a bucket of cleaning products"></div>
    <div class="hero-title abs">Reliable<br>Cleaners</div>
    <div class="hero-badge abs" role="img" aria-label="Orange starburst offer badge"></div>
    <div class="hero-badge-text abs">Introductory<br>Offer</div>
    <div class="hero-free abs">First Clean <b>FREE</b></div>
    <div class="hero-sub abs">Allow us to demonstrate our standards</div>
    <div class="dots abs"><span></span><span></span><span></span><span></span></div>
  </div>
</section>

<!-- Welcome -->
<h2 class="abs" style="left:88px;top:421px">Welcome!</h2>
<div class="welcome-photo abs" role="img" aria-label="Flat mop cleaning a wooden floor"></div>
<div class="abs para" style="left:88px;top:524px">
  <p class="intro-strong" style="margin-bottom:8px">Welcome to our website, we are a premier domestic cleaning company based in Elmford, Northvale.</p>
  <p><b style="font-size:10px;color:#333">Our vision</b> is to supply households with a quality, tailored cleaning service, freeing up individuals spare time and replacing the stereotypical unreliable, inconsistent cleaners.</p>
</div>
<a class="btn abs" href="#" style="left:87px;top:638px">More</a>

<!-- We Offer -->
<h2 class="abs" style="left:301px;top:421px">We Offer</h2>
<div class="abs" style="left:301px;top:445px;width:200px">
  <p class="intro-strong" style="margin-bottom:7px">We specialize in regular weekly cleans, however we also offer:</p>
  <ul class="list">
    <li>Bi-weekly Cleans</li><li>One-off Cleans</li><li>Spring Cleans</li><li>End of tenancy Cleans</li><li>After builders Cleans</li>
  </ul>
  <p>In order for us to understand exactly what you would like us to do, one of our team can visit you in-home at a time which is convenient for you to discuss your requirements.</p>
</div>
<a class="btn abs" href="#" style="left:300px;top:638px">More</a>

<!-- Quote -->
<h2 class="abs" style="left:515px;top:421px">Get a Quote Now</h2>
<form class="quote abs">
  <label>Name</label><div class="field"></div>
  <label>Email Address</label><div class="field"></div>
  <div class="field-row">
    <div><label>Phone</label><div class="field"></div></div>
    <div><label>Place</label><div class="field"></div></div>
  </div>
  <label>Choose Services</label>
  <div class="select"><span>Select Services</span><span>▾</span></div>
  <div style="text-align:right;margin-top:10px"><span class="btn-orange">Submit Quote</span></div>
</form>

<!-- Why Us -->
<h2 class="abs" style="left:88px;top:687px">Why Us</h2>
<div class="why-photo abs" role="img" aria-label="Cleaner mopping a warehouse floor with a yellow mop bucket"></div>
<div class="abs" style="left:193px;top:713px;width:205px">
  <ul class="list">
    <li>No contracts</li><li>Insured</li><li>Free Quotes</li><li>Personalised Service</li><li>We supply all Equipment at no Extra Cost</li><li>Hassel free service</li>
  </ul>
  <p>Have a look through our website to see how we can help you.</p>
</div>
<a class="btn abs" href="#" style="left:193px;top:875px">More</a>

<!-- Pricing -->
<h2 class="abs" style="left:413px;top:687px">Our Pricing</h2>
<div class="abs" style="left:413px;top:712px">
  <div class="price-row"><span>Regular and Bi-weekly services</span><span class="dash"></span><b>£10.00 p/h</b></div>
  <div style="text-align:right;width:297px;font-size:7.5px;font-style:italic;color:var(--link)">(minimum of 2 hrs)</div>
  <div class="price-row"><span>All other services</span><span class="dash"></span><b>£12.00 p/h</b></div>
  <div class="price-row" style="margin-top:4px"><span>Non domestic/ Commercial</span><span class="dash"></span><b>£14.00 p/h</b></div>
  <ul class="list" style="margin-top:8px;width:290px">
    <li>No hidden costs</li>
    <li>All prices agreed prior to commencing our work <span>– You know exactly what you will be paying.</span></li>
    <li>We invoice at the end of every fourth clean <span>– You do not have to worry about leaving payment each week.</span></li>
    <li>Choice of payment methods <span>– Cash, cheque or bank transfer.</span></li>
  </ul>
</div>
<a class="btn abs" href="#" style="left:639px;top:875px">More Details</a>

<!-- Footer -->
<footer class="site-footer abs">
  <h3 class="abs" style="left:87px;top:15px">Find our Location</h3>
  <div class="map abs" role="img" aria-label="Street map showing the company location"></div>
  <div class="abs small orange" style="left:201px;top:183px">Click for full Map</div>

  <h3 class="abs" style="left:300px;top:15px">Quick Contact</h3>
  <div class="abs" style="left:300px;top:42px">
    <div class="qfield" style="margin-bottom:9px">Name</div>
    <div class="qfield" style="margin-bottom:9px">Email</div>
    <div class="qfield" style="margin-bottom:9px">Phone</div>
    <div class="qfield" style="height:51px">Message</div>
  </div>
  <span class="btn-orange abs" style="left:418px;top:195px">Submit</span>

  <div class="abs" style="left:512px;top:15px;width:202px">
    <h4>Quick Links</h4>
    <p class="small">Home &nbsp;|&nbsp; Services &nbsp;|&nbsp; Prices &nbsp;|&nbsp; Contact Us</p>
    <h4 style="margin-top:8px">Other Services</h4>
    <p class="small">Office Cleaning | Aapartment Cleaning<br>Business Place Cleaning | Shopping Mall Cleaning</p>
    <div style="border-top:1px solid #666;margin:6px 0 8px"></div>
    <div style="font-family:'PT Sans',sans-serif;font-weight:700;font-size:14px;color:#777;display:flex;align-items:center;gap:5px;line-height:1"><span style="width:11px;height:11px;border-radius:50%;background:#777"></span>Brightwell Cleaners</div>
    <div class="small" style="color:#777;margin:2px 0 6px 54px;font-size:6.5px">Premier Domestic Cleaners</div>
    <h4>Contact Us</h4>
    <p class="small">For more information or if you would like to book a no obligatory in home visit, please do not hesitate to contact us on:</p>
    <p class="small" style="margin-top:4px">Telephone: <b class="orange" style="font-size:9px">07700900461</b></p>
    <p class="small" style="margin-top:4px">Email: <span class="orange" style="text-decoration:underline">brightwellcleaners@example.co.uk</span></p>
  </div>
</footer>
<div class="footer-bottom abs">
  <div class="abs small" style="left:87px;top:14px;font-weight:600">Copyright © 2012, Brightwell Cleaners . All Rights Reserved.</div>
  <div class="abs" style="left:500px;top:11px;display:flex;align-items:center;gap:10px;color:#fff;font-size:10px">
    Get Socialize with Us
    <div class="social"><span style="background:#3b5a98"></span><span style="background:#2aa9e0"></span><span style="background:#d9453a"></span><span style="background:#f29022"></span></div>
  </div>
</div>

</body>
</html>
```